Copper Harbor Athletics

COPPER HARBOR ATHLETICS PTY LTD, We are a revolutionary, fresh, new entity to the fitness industry looking to make a mark within and support local communities where we are situated. My business partner and i come with a broad range of skill sets and possess the ability and motivation to ensure our philosophy works - and the philosophy is simple - to help people improve their everyday life and well-being. Be it, helping them with their health and fitness, changing their appearance, improving motivation, setting and achieving goals or by helping them become part of a positive team atmosphere.
Our stores visual appearance, like our training concepts, is quite different to the normal run of the mill gym. It's fresh, it's vibrant, it looks great, and we know it will be a real head turner guaranteed to attract attention. This is definitely the future of fitness.
We would like to see on one side our Info and on the other side our LOGO, colour scheme is in the LOGO.
Final design should tell people "We Help People Stand Tall And Shine Like Copper!

Industry/Entity Type

Training

Contact Information for Business Card

Marcus
0417 362 591
marc@copperharborathletics.com.au
217 Glenview Rd East Balcombe NSW 2100

Requirements
Must have
• Our Logo

```html
<!DOCTYPE html>
<html lang="en">
<head>
<meta charset="utf-8">
<title>Copper Harbor Athletics — Business Card</title>
<link rel="stylesheet" href="https://fonts.googleapis.com/css2?family=Exo+2:wght@400;700;800&display=swap">
<style>
  :root {
    --backdrop: #1a1a1b;
    --card: #2d2d2f;
    --card-edge: #3a3a3c;
    --ink: #f2f2f2;
    --ink-soft: #d9d9d9;
    --accent: #d8322b;
    --mark: #d8322b;
  }
  * { margin: 0; padding: 0; box-sizing: border-box; }
  html, body {
    width: 1200px;
    height: 900px;
    overflow: hidden;
    background: var(--backdrop);
    font-family: "Exo 2", Arial, sans-serif;
    color: var(--ink);
  }
  .canvas {
    position: relative;
    width: 1200px;
    height: 900px;
  }
  .card {
    position: absolute;
    left: 270px;
    width: 660px;
    height: 400px;
    background: var(--card);
    border: 1px solid var(--card-edge);
    box-shadow: 0 18px 40px rgba(0, 0, 0, 0.55);
  }
  .card--front { top: 40px; }
  .card--back  { top: 470px; }

  /* Front: brand lockup */
  .brand {
    position: absolute;
    left: 50%;
    top: 50%;
    transform: translate(-50%, -50%);
    display: flex;
    align-items: center;
    gap: 34px;
  }
  .brand__square {
    width: 150px;
    height: 150px;
    background: var(--mark);
    flex: none;
  }
  .brand__name {
    font-weight: 800;
    font-size: 50px;
    line-height: 1.02;
    letter-spacing: 1px;
    text-transform: uppercase;
    color: var(--ink);
  }

  /* Back: contact side */
  .contact {
    position: absolute;
    left: 56px;
    top: 150px;
  }
  .contact__name {
    font-weight: 800;
    font-size: 70px;
    line-height: 1;
    letter-spacing: 2px;
    text-transform: uppercase;
    color: var(--ink);
    padding-bottom: 8px;
    border-bottom: 2px solid var(--accent);
    width: 300px;
  }
  .contact__list {
    list-style: none;
    margin-top: 16px;
  }
  .contact__item {
    display: flex;
    align-items: center;
    gap: 12px;
    font-weight: 700;
    font-size: 17px;
    line-height: 1.15;
    color: var(--ink-soft);
    margin-bottom: 12px;
  }
  .contact__icon {
    width: 20px;
    height: 20px;
    flex: none;
    fill: var(--accent);
  }
  .back-brand {
    position: absolute;
    right: 56px;
    top: 66px;
    display: flex;
    flex-direction: column;
    align-items: center;
    gap: 12px;
  }
  .back-brand__square {
    width: 120px;
    height: 120px;
    background: var(--mark);
  }
  .back-brand__name {
    font-weight: 800;
    font-size: 15px;
    letter-spacing: 1px;
    text-transform: uppercase;
    color: var(--ink);
    text-align: center;
    line-height: 1.15;
  }
</style>
</head>
<body>
<main class="canvas">

  <section class="card card--front" aria-label="Card front">
    <div class="brand">
      <div class="brand__square" aria-hidden="true"></div>
      <div class="brand__name">Copper<br>Harbor<br>Athletics</div>
    </div>
  </section>

  <section class="card card--back" aria-label="Card back">
    <div class="contact">
      <h1 class="contact__name">Marcus</h1>
      <ul class="contact__list">
        <li class="contact__item">
          <svg class="contact__icon" viewBox="0 0 24 24" aria-hidden="true"><path d="M6.6 10.8a15.1 15.1 0 0 0 6.6 6.6l2.2-2.2a1 1 0 0 1 1-.25 11.4 11.4 0 0 0 3.6.57 1 1 0 0 1 1 1V20a1 1 0 0 1-1 1A17 17 0 0 1 3 4a1 1 0 0 1 1-1h3.5a1 1 0 0 1 1 1c0 1.25.2 2.45.57 3.57a1 1 0 0 1-.25 1z"/></svg>
          <span>0417 362 591</span>
        </li>
        <li class="contact__item">
          <svg class="contact__icon" viewBox="0 0 24 24" aria-hidden="true"><path d="M12 3 2 12h3v8h5v-6h4v6h5v-8h3z"/></svg>
          <span>217 Glenview Rd<br>East Balcombe NSW 2100</span>
        </li>
        <li class="contact__item">
          <svg class="contact__icon" viewBox="0 0 24 24" aria-hidden="true"><path d="M3 5h18a1 1 0 0 1 1 1v12a1 1 0 0 1-1 1H3a1 1 0 0 1-1-1V6a1 1 0 0 1 1-1zm9 7.2L4 7.5V9l8 4.7L20 9V7.5z"/></svg>
          <span>marc@copperharborathletics.com.au</span>
        </li>
      </ul>
    </div>
    <div class="back-brand">
      <div class="back-brand__square" aria-hidden="true"></div>
      <div class="back-brand__name">Copper Harbor<br>Athletics</div>
    </div>
  </section>

</main>
</body>
</html>
```